Kickass billboard for motorway

Fix my old hauler - clue is in the name.
We have a 45ft billboard we're looking to design constructed from an old trailer we own (so we can be as creative as possible).
We provide a van buying service, being one of the only companies in the UK with the facilities to recover faulty, damaged and broken vans - from small car derived vans to large trucks and lorries.
ur niche in the market is different to car buying services, as buying and selling cars is often an emotionally driven process, whereas people often see and treat vans purely as a tool. There are alternatives to a car, public transport etc, but not to a work van - so people go out straight away and replace them immediately, often leaving the old broken van to sit on their drive or in their unit.
Looking to start building a brand asset bank.
Feel free to check out our website to get a feel for what we do:
Fixmyoldhauler.co.uk

Target Market(s)

Van owners/drivers & fleet managers

Industry/Entity Type

Automotive

Font styles to use
Sans Serif

Colors
34a7d8

Requirements
Must have
• Eye-catching - very eye-catching.
We want to advertise the fact we collect vehicles for free.
We pay instantly upon arrival.
Our phone number 0161 493 7062
Our website www.fixmyoldhauler.co.uk
Nice to have
• 3d elements - we have the ability to get 3d props for the billboard including damaged vans etc.

```html
<!DOCTYPE html>
<html lang="en">
<head>
<meta charset="utf-8">
<title>Fix my old hauler – Motorway Billboard</title>
<link rel="stylesheet" href="https://fonts.googleapis.com/css2?family=Oswald:wght@500;700&family=Roboto:wght@500;700;900&display=swap">
<style>
  :root {
    --brand-blue: #34a7d8;
    --panel-blue: #56b0e4;
    --ink: #1a1a1a;
    --paper: #ffffff;
    --stage-dark: #333333;
    --stage-light: #7a7a7a;
  }
  html, body {
    margin: 0;
    padding: 0;
    width: 1200px;
    height: 967px;
    overflow: hidden;
  }
  body {
    background: linear-gradient(110deg, var(--stage-dark) 0%, #555 55%, var(--stage-light) 100%);
    position: relative;
  }
  .billboard {
    position: absolute;
    left: 50px;
    top: 335px;
    width: 1100px;
    height: 297px;
    box-shadow: 0 30px 40px rgba(0,0,0,0.35);
  }
  .billboard svg { display: block; width: 100%; height: 100%; }
  .headline { font-family: "Oswald", sans-serif; font-weight: 700; }
  .condensed-italic { font-family: "Oswald", sans-serif; font-weight: 700; }
  .brand-name { font-family: "Roboto", sans-serif; font-weight: 700; }
  .web-address { font-family: "Roboto", sans-serif; font-weight: 500; }
  .phone-number { font-family: "Roboto", sans-serif; font-weight: 900; }
</style>
</head>
<body>
  <div class="billboard">
    <svg viewBox="0 0 1815 490" xmlns="http://www.w3.org/2000/svg">
      <defs>
        <linearGradient id="paper-fade" x1="0" y1="0" x2="1" y2="1">
          <stop offset="0" stop-color="#ffffff"/>
          <stop offset="0.5" stop-color="#f1f1f1"/>
          <stop offset="1" stop-color="#ffffff"/>
        </linearGradient>
        <linearGradient id="headline-fill" x1="0" y1="0" x2="0" y2="1">
          <stop offset="0" stop-color="#ffffff"/>
          <stop offset="1" stop-color="#c9c9c9"/>
        </linearGradient>
      </defs>

      <!-- base -->
      <rect class="base" width="1815" height="490" fill="url(#paper-fade)"/>

      <!-- headline band -->
      <polygon class="headline-band" points="0,40 1095,40 1015,237 0,237" fill="var(--ink)"/>
      <text class="headline" x="70" y="195" font-size="158" textLength="895" lengthAdjust="spacingAndGlyphs" fill="url(#headline-fill)">SELL YOUR VAN</text>

      <!-- condition band -->
      <polygon class="condition-band" points="125,218 880,218 910,315 150,315" fill="var(--panel-blue)"/>
      <text class="condensed-italic" transform="translate(188,300) skewX(-12)" font-size="78" textLength="655" lengthAdjust="spacingAndGlyphs" fill="var(--paper)">IN ANY CONDITION</text>

      <!-- brand name -->
      <rect class="brand-mark" x="75" y="362" width="62" height="62" fill="var(--panel-blue)"/>
      <text class="brand-name" x="160" y="422" font-size="76" textLength="780" lengthAdjust="spacingAndGlyphs" fill="var(--ink)">fixmyoldhauler</text>

      <!-- offer panel -->
      <polygon class="offer-panel" points="1170,0 1815,0 1815,365 1030,365" fill="var(--panel-blue)"/>
      <polygon class="divider-stripe" points="1072,210 1088,210 985,490 955,490" fill="var(--ink)"/>

      <text class="web-address" x="1480" y="82" font-size="34" text-anchor="middle" fill="var(--ink)">www.fixmyoldhauler.co.uk</text>

      <polygon class="pay-box" points="1178,124 1765,124 1737,213 1148,213" fill="var(--ink)"/>
      <text class="condensed-italic" transform="translate(1460,196) skewX(-12)" font-size="68" text-anchor="middle" textLength="520" lengthAdjust="spacingAndGlyphs" fill="var(--paper)">WE PAY INSTANTLY</text>

      <polygon class="arrival-box" points="1290,208 1672,208 1650,268 1260,268" fill="var(--paper)"/>
      <text class="condensed-italic" transform="translate(1465,258) skewX(-12)" font-size="52" text-anchor="middle" textLength="330" lengthAdjust="spacingAndGlyphs" fill="var(--panel-blue)">UPON ARRIVAL</text>

      <text class="condensed-italic" transform="translate(1442,336) skewX(-12)" font-size="48" text-anchor="middle" textLength="615" lengthAdjust="spacingAndGlyphs" fill="var(--paper)">We Collect Vehicles For Free.</text>

      <!-- phone strip -->
      <polygon class="phone-strip" points="1030,365 1815,365 1815,468 993,468" fill="var(--paper)"/>
      <polygon class="bottom-bar" points="993,468 1815,468 1815,490 985,490" fill="var(--panel-blue)"/>

      <g class="phone-icon">
        <circle cx="1088" cy="415" r="44" fill="var(--panel-blue)" stroke="var(--ink)" stroke-width="7"/>
        <path d="M1074 390 q-10 6 -6 22 q6 20 24 30 q12 6 18 -4 l-9 -9 q-5 4 -9 1 q-10 -7 -14 -17 q-2 -5 3 -8 z" fill="var(--paper)"/>
      </g>
      <text class="phone-number" x="1165" y="447" font-size="84" textLength="585" lengthAdjust="spacingAndGlyphs" fill="var(--ink)">0161 493 7062</text>
    </svg>
  </div>
</body>
</html>
```